Tellory Yard Supplies needs a spring flyer

We are a local garden centre in Mississauga, Ontario. The product we want to promote is our disposal boxes. These are boxes that can be used to dispose cleanfill, concrete, asphalt, renovation material. Sizes range from 4 yard to 40 yard bins. They can also serve a dual purpose! When customers order a box they can also order any bulk material that we carry to go in the box and essentially get a free delivery. Example: If a customer orders a 4 yard disposal box, they can get up to 4 yards of any material we carry (soils, mulches, gravels) put in the box at the time of delivery. They will only pay the price of the box and the price of the material the delivery is FREE. We would like to see designs that use the colour green. The final design should communicate FREE delivery with box rentals and reliable service! For more information visit our website www.tellorygrounds.example

Target Market(s)

target customer for this flyer is home owners. This will be distributed by mail. Needs to standout amongst all other mail flyers!

Industry/Entity Type

Concrete

Requirements
Must have
• company phone number 555-184-6730

Must have PROMO CODE: QLPEN7093
Nice to have
• a map pin pointing our location 8162 Quenby Road, Mississauga, Ontario Canada

```html
<!DOCTYPE html>
<html lang="en">
<head>
<meta charset="utf-8">
<title>Tellory Yard Supplies – Mini Disposal Box</title>
<link rel="stylesheet" href="https://fonts.googleapis.com/css2?family=Noto+Serif:wght@300;400&family=Tinos&display=swap">
<style>
  :root {
    --green: #1b9248;
    --green-dark: #0f6e35;
    --green-light: #3fae6c;
    --frame-green: #9fcaa9;
    --box-blue: #262e7a;
    --box-blue-dark: #1a1f5a;
    --paper: #ffffff;
    --page-bg: #eef0ee;
    --ink: #111111;
  }
  * { margin: 0; padding: 0; box-sizing: border-box; }
  html, body { width: 1200px; height: 1000px; overflow: hidden; background: var(--page-bg); }
  .flyer {
    position: absolute; left: 113px; top: 185px; width: 945px; height: 663px;
    background: var(--paper); border: 2px solid var(--green);
    font-family: "Noto Serif", Georgia, serif; color: var(--green);
  }
  .flyer > * { position: absolute; }
  .box-photo {
    left: 4px; top: 4px; width: 931px; height: 441px;
    background: linear-gradient(180deg, var(--box-blue) 0%, #2d3690 50%, var(--box-blue-dark) 100%);
  }
  .brand-shape { left: 0; top: 0; width: 945px; height: 663px; }
  .brand-badge {
    left: 68px; top: 37px; width: 146px; height: 100px; border-radius: 50%;
    background: var(--paper); border: 2px solid var(--green-dark);
    display: flex; flex-direction: column; align-items: center; justify-content: center; text-align: center;
    color: var(--green-dark); font-size: 12px; line-height: 1.25; padding: 0 10px;
  }
  .brand-badge .phone { font-size: 10px; margin-top: 4px; }
  .title { left: 230px; top: 22px; font-size: 46px; font-weight: 300; color: var(--green); -webkit-text-stroke: 0.6px var(--green-dark); white-space: nowrap; }
  .lead { font-size: 30px; font-weight: 300; color: var(--green); white-space: nowrap; line-height: 1; }
  .lead-buy { left: 247px; top: 85px; }
  .lead-rent { left: 265px; top: 240px; font-size: 27px; }
  .lead-empty { left: 314px; top: 273px; font-size: 27px; }
  .material {
    background: var(--paper); border: 1px solid var(--green-dark); border-radius: 50%;
    display: flex; align-items: center; justify-content: center;
    font-size: 21px; color: var(--green); white-space: nowrap;
  }
  .m-concrete { left: 260px; top: 130px; width: 112px; height: 40px; }
  .m-shingles { left: 410px; top: 122px; width: 196px; height: 50px; }
  .m-asphalt { left: 265px; top: 190px; width: 112px; height: 42px; }
  .m-fill { left: 410px; top: 189px; width: 242px; height: 60px; }
  .m-garbage { left: 281px; top: 308px; width: 372px; height: 68px; }
  .truck-photo {
    width: 186px; height: 141px; border: 4px solid var(--green);
    background: linear-gradient(180deg, #d9dbd6 0%, #c4c6c0 55%, #8f8a84 100%);
  }
  .truck-loaded { left: 677px; top: 24px; }
  .truck-empty { left: 677px; top: 234px; }
  .sizes { left: 686px; top: 172px; font-size: 18px; font-weight: 300; color: var(--green-light); line-height: 1.2; }
  .contact {
    left: 23px; top: 218px; font-family: "Tinos", "Times New Roman", serif;
    font-size: 15.5px; line-height: 19.8px; color: var(--ink);
  }
  .contact .promo { margin-top: 38px; }
  .offer-frame {
    left: 22px; top: 450px; width: 390px; height: 205px;
    border: 20px solid var(--frame-green); border-radius: 28px; background: var(--paper);
  }
  .offer-text {
    left: 50px; top: 480px; width: 342px; font-size: 26.5px; line-height: 34.5px;
    color: var(--green); text-align: justify;
  }
  .map-panel { left: 464px; top: 392px; width: 465px; height: 263px; border: 3px solid var(--green); background: #eceae4; }
  .map-overlay { left: 464px; top: 392px; width: 465px; height: 263px; }
  .map-caption { left: 502px; top: 575px; font-size: 52px; color: var(--green); white-space: nowrap; line-height: 1; }
</style>
</head>
<body>
  <main class="flyer">
    <div class="box-photo" role="img" aria-label="Photo of a blue steel disposal bin"></div>

    <svg class="brand-shape" viewBox="0 0 945 663" aria-hidden="true">
      <polygon points="59,20 145,20 100,220 262,220 262,405 17,405 17,220" fill="var(--green)" stroke="#0c4d26" stroke-width="1"/>
    </svg>

    <div class="brand-badge">
      <span>Tellory Yard Supplies Co. Ltd.</span>
      <span class="phone">(555) 184-6730</span>
    </div>

    <h1 class="title">Mini Disposal Box</h1>
    <p class="lead lead-buy">You can buy fullfil with:</p>

    <div class="material m-concrete">Concrete</div>
    <div class="material m-shingles">Roofing Shingles</div>
    <div class="material m-asphalt">Asphalt</div>
    <div class="material m-fill">Clean Fill (Soil &amp; Sod)</div>

    <p class="lead lead-rent">or just rent it</p>
    <p class="lead lead-empty">empty to fullfill with:</p>
    <div class="material m-garbage">Garbage (construction materials)</div>

    <div class="truck-photo truck-loaded" role="img" aria-label="Photo of a delivery truck carrying a loaded disposal box"></div>
    <p class="sizes">Sizes range is<br>from 4 to 40 yards</p>
    <div class="truck-photo truck-empty" role="img" aria-label="Photo of a delivery truck carrying an empty disposal box"></div>

    <address class="contact" style="font-style:normal">
      8162 Quenby Road,<br>
      Mississauga, ON L5X 0Q4<br>
      Tel: 555-184-6730<br>
      Fax: 555-291-4058<br>
      email: info@tellorygrounds.example
      <p class="promo">when ordering use this<br>POROMOCODE: QLPEN7093</p>
    </address>

    <div class="offer-frame"></div>
    <p class="offer-text">If you order a box and also any bulk material, we carry to go in the box and you get a free delivery</p>

    <div class="map-panel" role="img" aria-label="Street map showing the yard location on Quenby Road, Mississauga"></div>
    <svg class="map-overlay" viewBox="0 0 465 263" aria-hidden="true">
      <rect x="123" y="68" width="73" height="38" fill="none" stroke="var(--green)" stroke-width="1.5"/>
      <circle cx="100" cy="188" r="8.5" fill="none" stroke="var(--green)" stroke-width="2"/>
      <line x1="106" y1="180" x2="168" y2="86" stroke="var(--green)" stroke-width="3"/>
      <polygon points="173,78 158,86 170,94" fill="var(--green)"/>
    </svg>
    <p class="map-caption">here we are</p>
  </main>
</body>
</html>
```